Business Card Design

Design new business card using new logo attached and some details as old business card, which is also attached.

Industry/Entity Type

Business

```html
<!DOCTYPE html>
<html lang="en">
<head>
<meta charset="utf-8">
<title>DRW Business Card</title>
<link href="https://fonts.googleapis.com/css2?family=Cinzel:wght@400;600&family=Michroma&display=swap" rel="stylesheet">
<style>
  :root {
    --navy: #14127a;
    --grey: #6f6f73;
    --rule: #b9b9bd;
    --paper: #fbfbfb;
    --backdrop: #e9e7e3;
  }
  * { box-sizing: border-box; margin: 0; padding: 0; }
  html, body {
    width: 1200px; height: 800px; overflow: hidden;
    background: var(--backdrop);
  }
  .stage {
    width: 1200px; height: 800px;
    display: flex; align-items: center; justify-content: center;
  }
  .card {
    position: relative;
    width: 1000px; height: 572px;
    background: var(--paper);
    box-shadow: 0 12px 30px rgba(0,0,0,.18);
    overflow: hidden;
  }
  .card__band {
    position: absolute; left: 0; top: 0; bottom: 0;
    width: 30px; background: var(--navy);
  }

  /* brand block */
  .brand {
    position: absolute; left: 120px; top: 290px;
    display: flex; align-items: center;
  }
  .brand__name {
    font-family: "Cinzel", serif; font-weight: 600;
    font-size: 70px; color: var(--navy); letter-spacing: 2px;
  }
  .brand__divider {
    width: 1px; height: 100px; background: var(--rule);
    margin: 0 22px 0 24px;
  }
  .brand__tagline {
    font-family: "Cinzel", serif; color: var(--navy);
    font-size: 26px; line-height: 1.05;
  }
  .brand__owner {
    font-family: "Cinzel", serif; color: var(--grey);
    font-size: 17px; letter-spacing: 1px; margin-top: 8px;
  }

  /* contact block */
  .contact {
    position: absolute; left: 590px; top: 80px;
    font-family: "Michroma", sans-serif;
  }
  .contact__name { color: var(--navy); font-size: 19px; }
  .contact__creds { color: var(--grey); font-size: 19px; margin: 6px 0 0 28px; }
  .contact__address {
    color: var(--grey); font-size: 17px; line-height: 1.5;
    margin: 22px 0 0 60px;
  }
  .contact__rows {
    display: flex; margin: 24px 0 0 60px;
  }
  .contact__labels {
    color: var(--navy); font-size: 16px; font-weight: 700;
    line-height: 1.75; padding-right: 16px;
    border-right: 1px solid var(--rule);
  }
  .contact__values {
    color: var(--grey); font-size: 16px; line-height: 1.75;
    padding-left: 30px;
  }
</style>
</head>
<body>
<main class="stage">
  <article class="card">
    <div class="card__band"></div>

    <section class="brand">
      <div class="brand__name">DRW</div>
      <div class="brand__divider"></div>
      <div class="brand__text">
        <div class="brand__tagline">TAX, ACCOUNTING &amp;<br>ADVISORY SERVICES</div>
        <div class="brand__owner">DANA R. WHITFIELD, CPA, PA</div>
      </div>
    </section>

    <section class="contact">
      <div class="contact__name">Dana Whitfield,</div>
      <div class="contact__creds">CPA,CVA</div>
      <div class="contact__address">
        214 Harbor Point Ave.<br>Seaside Bay, FL 32400
      </div>
      <div class="contact__rows">
        <div class="contact__labels">Office:<br>Mobile:<br>Email:<br>Web:</div>
        <div class="contact__values">(555)010-2040<br>(555)-014-7788<br>dana@drwcpafirm.com<br>www.drwcpafirm.com</div>
      </div>
    </section>
  </article>
</main>
</body>
</html>
```